Brinvale LLC Website Redesign Productct (HTML/CSS NEEDED)

We are looking for a new website to replace our current site www.brinvalecare.example. We would like to be able to offer richer content with more pictures as well as create a design that integrates with our new logo (attached).

Target Market(s)

Our target market consists of home care agencies, and human services not for profits.

Font styles to use
Sans Serif

Requirements
Must have
• Design integrated with new logo

```html
<!DOCTYPE html>
<html lang="en">
<head>
<meta charset="utf-8">
<title>Brinvale – Healthcare Management System</title>
<link href="https://fonts.googleapis.com/css2?family=Open+Sans:wght@400;600;700;800&display=swap" rel="stylesheet">
<style>
:root{
  --blue:#1d86d1;
  --blue-dark:#13629e;
  --navy:#15263b;
  --navy-deep:#0e1a29;
  --ink:#3b4653;
  --muted:#7b8794;
  --line:#d9e2ea;
  --soft:#f1f4f7;
  --accent:#f08a24;
  --white:#ffffff;
}
*{box-sizing:border-box;margin:0;padding:0}
html,body{width:1200px;height:2304px;overflow:hidden}
body{font-family:"Open Sans",Arial,sans-serif;color:var(--ink);background:var(--white);font-size:13px;line-height:1.55}
.wrap{width:1080px;margin:0 auto;position:relative}

.site-header{height:56px;border-bottom:1px solid var(--line)}
.site-header .wrap{display:flex;align-items:center;justify-content:space-between;height:56px}
.brand{display:flex;align-items:center;gap:8px;font-size:26px;font-weight:700;color:var(--blue)}
.brand-dot{width:14px;height:14px;border-radius:50%;background:var(--blue)}
.header-right{display:flex;flex-direction:column;align-items:flex-end;gap:4px}
.phone{font-size:11px;color:var(--muted)}
.nav{display:flex;gap:2px}
.nav a{font-size:12px;color:var(--ink);text-decoration:none;padding:5px 12px}
.nav a.active{background:var(--blue);color:var(--white)}

.hero{height:520px;position:relative;background:linear-gradient(100deg,#dbe7f1 0%,#b9cfe2 45%,#6f8fae 100%)}
.hero-art{position:absolute;inset:0}
.hero-copy{position:absolute;left:150px;top:60px;width:470px}
.hero-title{background:var(--blue);color:var(--white);font-size:31px;font-weight:700;line-height:1.25;padding:12px 18px;text-transform:uppercase}
.hero-text{background:rgba(255,255,255,.85);font-size:16px;padding:14px 18px;color:var(--ink)}
.btn{display:inline-block;background:var(--blue);color:var(--white);font-size:12px;font-weight:700;text-transform:uppercase;padding:8px 18px;border-radius:3px;text-decoration:none}
.hero .btn{margin:14px 0 0 18px}
.slide-arrow{position:absolute;top:236px;width:36px;height:48px;background:rgba(21,38,59,.7);display:flex;align-items:center;justify-content:center}
.slide-arrow.left{left:0}.slide-arrow.right{right:0}

.section-head{display:flex;align-items:center;gap:18px;margin-bottom:16px}
.section-head::before,.section-head::after{content:"";flex:1;height:1px;background:var(--line)}
.section-head h2{font-size:24px;font-weight:700;color:var(--navy);text-transform:uppercase;letter-spacing:.5px}
.section-head h2 span{color:var(--blue)}

.about{padding:28px 0 10px;height:300px}
.about p{font-size:13px;color:var(--ink)}
.about p b{color:var(--blue)}
.ticks{display:grid;grid-template-columns:1fr 1fr;gap:10px 40px;margin:22px 100px 0}
.ticks li{list-style:none;display:flex;align-items:center;gap:10px;font-size:13px;font-weight:600;color:var(--navy)}

.features{height:330px;display:grid;grid-template-columns:repeat(3,1fr);gap:24px}
.card{border:1px solid var(--line);background:var(--white);position:relative;height:300px}
.card h3{background:var(--blue);color:var(--white);text-transform:uppercase;font-size:15px;font-weight:700;text-align:center;padding:8px 0}
.card-media{height:120px;background:linear-gradient(135deg,#cfdfec,#7fa6c7)}
.card-media.training{background:linear-gradient(135deg,#e9eef2,#a8bccd)}
.card-media.news{background:linear-gradient(135deg,#f3d6d6,#d26b6b)}
.card p{font-size:11.5px;padding:10px 14px;color:var(--ink)}
.card .btn{position:absolute;left:50%;transform:translateX(-50%);bottom:-14px;background:var(--navy);font-size:11px;padding:6px 22px}

.how{height:370px;padding-top:24px}
.steps{display:grid;grid-template-columns:repeat(4,1fr);gap:40px;margin-top:20px;position:relative}
.steps::before{content:"";position:absolute;top:55px;left:130px;right:130px;border-top:2px dashed var(--line)}
.step{text-align:center;position:relative}
.step-icon{width:110px;height:110px;border-radius:50%;background:var(--blue);border:6px solid #d6e8f6;margin:0 auto 14px;display:flex;align-items:center;justify-content:center}
.step h4{font-size:17px;font-weight:800;color:var(--blue);text-transform:uppercase;margin-bottom:6px}
.step p{font-size:11.5px;color:var(--muted)}

.clients{height:230px;background:var(--soft);padding-top:20px}
.quote{display:flex;gap:26px;align-items:flex-start;margin:6px 40px 0}
.avatar{flex:none;width:96px;height:96px;border-radius:50%;background:linear-gradient(135deg,#c9d3dc,#8a9aa9);border:4px solid var(--white)}
.quote-box{background:var(--white);border:1px solid var(--line);padding:14px 18px;font-size:12px;color:var(--ink)}
.quote-by{margin-top:8px;font-size:12px;color:var(--blue);font-weight:700}
.quote-more{float:right;font-size:11px;color:var(--muted)}

.partners{height:170px;padding-top:26px}
.partners h2 span{color:var(--accent)}
.badges{display:flex;justify-content:space-between;align-items:center;margin:22px 20px 0}
.badge{width:130px;height:40px;background:#c6ccd3;border-radius:4px}

.footer-wave{display:block;height:40px;width:1200px}
.site-footer{background:var(--navy);color:#c9d3de;height:200px;padding-top:12px}
.footer-cols{display:grid;grid-template-columns:200px 1fr 340px;gap:40px}
.site-footer h5{color:var(--white);font-size:15px;font-weight:700;margin-bottom:10px}
.links li{list-style:none;font-size:12px;line-height:1.75}
.contact{display:flex;gap:16px}
.contact ul li{list-style:none;display:flex;gap:8px;align-items:center;font-size:12px;margin-bottom:7px}
.map{width:200px;height:120px;background:linear-gradient(135deg,#dfe6d9,#b9c9d6);border-radius:2px}
.newsletter p{font-size:12px;margin-bottom:10px}
.subscribe{display:flex}
.subscribe span{flex:1;background:var(--white);color:var(--muted);font-size:11px;padding:7px 10px}
.subscribe b{background:var(--blue);color:var(--white);font-size:11px;padding:7px 12px}
.social{display:flex;gap:8px;align-items:center;margin-top:14px;font-size:12px}
.social i{width:22px;height:22px;border-radius:50%;background:var(--blue);display:block}
.footer-bar{background:var(--navy-deep);height:38px;color:#8797a8;font-size:11px}
.footer-bar .wrap{display:flex;justify-content:space-between;align-items:center;height:38px}
.footer-bar .brand{font-size:18px;color:var(--white)}
.footer-bar .brand-dot{width:10px;height:10px}
</style>
</head>
<body>

<header class="site-header">
  <div class="wrap">
    <div class="brand"><span class="brand-dot"></span>Brinvale</div>
    <div class="header-right">
      <div class="phone">1-800-555-0142 &nbsp;|&nbsp; hello@brinvalecare.example</div>
      <nav class="nav">
        <a class="active">Home</a><a>How it Works</a><a>Services</a><a>Training and Transition</a><a>Latest News</a><a>Contact Us</a>
      </nav>
    </div>
  </div>
</header>

<section class="hero">
  <div class="hero-art" role="img" aria-label="Businessman pointing at a glowing growth chart"></div>
  <div class="hero-copy">
    <h1 class="hero-title">Brinvale is a healthcare management system</h1>
    <p class="hero-text">Brinvale is a healthcare management system designed specifically for the purpose of helping healthcare companies manage their agency.</p>
    <a class="btn">Read more ›</a>
  </div>
  <div class="slide-arrow left"><svg width="12" height="18"><path d="M10 2 3 9l7 7" stroke="#fff" stroke-width="3" fill="none"/></svg></div>
  <div class="slide-arrow right"><svg width="12" height="18"><path d="M2 2l7 7-7 7" stroke="#fff" stroke-width="3" fill="none"/></svg></div>
</section>

<section class="about">
  <div class="wrap">
    <div class="section-head"><h2>About <span>Brinvale</span></h2></div>
    <p>Brinvale is a <b>web-based healthcare management</b> platform specifically designed to streamline business processes, maximise billable hours, manage compliance, and adapt to a changing regulatory environment. At Brinvale our goal is to increase your bottom line while increasing efficiency and quality of care from day one. That is why we do not charge burdensome setup fees, and why our team walks with you through every stage of training, transition and daily operations across your whole agency.</p>
    <ul class="ticks">
      <li><svg width="18" height="18"><circle cx="9" cy="9" r="9" fill="#1d86d1"/><path d="M5 9l3 3 5-6" stroke="#fff" stroke-width="2" fill="none"/></svg>Improve Quality Of Service</li>
      <li><svg width="18" height="18"><circle cx="9" cy="9" r="9" fill="#1d86d1"/><path d="M5 9l3 3 5-6" stroke="#fff" stroke-width="2" fill="none"/></svg>Increase Compliance And Strengthen Management Of Fraud And Abuse</li>
      <li><svg width="18" height="18"><circle cx="9" cy="9" r="9" fill="#1d86d1"/><path d="M5 9l3 3 5-6" stroke="#fff" stroke-width="2" fill="none"/></svg>Improve Efficiency Of Operational Processes</li>
      <li><svg width="18" height="18"><circle cx="9" cy="9" r="9" fill="#1d86d1"/><path d="M5 9l3 3 5-6" stroke="#fff" stroke-width="2" fill="none"/></svg>Provide Immediate Return On Investment By Minimizing Upfront Costs</li>
    </ul>
  </div>
</section>

<section class="wrap features">
  <article class="card">
    <h3>Our Services</h3>
    <div class="card-media" role="img" aria-label="Care staff reviewing records together"></div>
    <p>Improving an agency's quality of care, financial and operational performance, and compliance is the primary mission of our team.</p>
    <a class="btn">Read more</a>
  </article>
  <article class="card">
    <h3>Training and Transition</h3>
    <div class="card-media training" role="img" aria-label="Team in a training session"></div>
    <p>At Brinvale we understand that a system, no matter how powerful, can only increase productivity to the extent that it is used well.</p>
    <a class="btn">Read more</a>
  </article>
  <article class="card">
    <h3>Latest News</h3>
    <div class="card-media news" role="img" aria-label="Red heart and stethoscope"></div>
    <p>January 3, 2015 — Brinvale is sponsoring the Northfield Care Network Conference in Riverton this year.</p>
    <a class="btn">Read more</a>
  </article>
</section>

<section class="how">
  <div class="wrap">
    <div class="section-head"><h2>How it <span>Works</span></h2></div>
    <div class="steps">
      <div class="step">
        <div class="step-icon"><svg width="40" height="50" viewBox="0 0 40 50"><path d="M20 2C10 2 3 9 3 19c0 13 17 29 17 29s17-16 17-29C37 9 30 2 20 2z" fill="#fff"/><circle cx="20" cy="19" r="7" fill="#1d86d1"/></svg></div>
        <h4>Tracking</h4>
        <p>Lorem set amet at ornare sapien, quis nostrud exerci tation ullamcorper suscipit lobortis nisl ut aliquip.</p>
      </div>
      <div class="step">
        <div class="step-icon"><svg width="46" height="44" viewBox="0 0 46 44"><rect x="3" y="6" width="40" height="36" rx="3" fill="#fff"/><rect x="3" y="6" width="40" height="9" fill="#cfe4f5"/><rect x="11" y="1" width="4" height="10" fill="#fff"/><rect x="31" y="1" width="4" height="10" fill="#fff"/><g fill="#1d86d1"><rect x="9" y="20" width="6" height="5"/><rect x="20" y="20" width="6" height="5"/><rect x="31" y="20" width="6" height="5"/><rect x="9" y="30" width="6" height="5"/><rect x="20" y="30" width="6" height="5"/></g></svg></div>
        <h4>Scheduling</h4>
        <p>Lorem set amet at ornare sapien, quis nostrud exerci tation ullamcorper suscipit lobortis nisl ut aliquip.</p>
      </div>
      <div class="step">
        <div class="step-icon"><svg width="44" height="44" viewBox="0 0 44 44"><circle cx="22" cy="22" r="20" fill="#fff"/><text x="22" y="31" text-anchor="middle" font-family="Open Sans,Arial,sans-serif" font-size="26" font-weight="800" fill="#1d86d1">$</text></svg></div>
        <h4>Payroll</h4>
        <p>Lorem set amet at ornare sapien, quis nostrud exerci tation ullamcorper suscipit lobortis nisl ut aliquip.</p>
      </div>
      <div class="step">
        <div class="step-icon"><svg width="38" height="46" viewBox="0 0 38 46"><path d="M2 2h24l10 10v32H2z" fill="#fff"/><g stroke="#1d86d1" stroke-width="3"><path d="M8 18h22M8 26h22M8 34h14"/></g></svg></div>
        <h4>Billing</h4>
        <p>Lorem set amet at ornare sapien, quis nostrud exerci tation ullamcorper suscipit lobortis nisl ut aliquip.</p>
      </div>
    </div>
  </div>
</section>

<section class="clients">
  <div class="wrap">
    <div class="section-head"><h2>What our <span>Clients Say</span></h2></div>
    <div class="quote">
      <div class="avatar" role="img" aria-label="Client portrait"></div>
      <div>
        <div class="quote-box">We switched to Brinvale because there is no other system that possesses the business processes to manage the regulatory requirements which are common in our state. The bottom line allows us to retrieve information required to remain in compliance and to manage the demands of an audit. Overall, Brinvale has helped us cut costs, become more organised, maximise our billable hours and strengthen our compliance program.</div>
        <div class="quote-by">— Dana Holt, Administrator <span class="quote-more">Read more testimonials ›</span></div>
      </div>
    </div>
  </div>
</section>

<section class="partners">
  <div class="wrap">
    <div class="section-head"><h2>Our <span>Partners</span></h2></div>
    <div class="badges">
      <div class="badge"></div><div class="badge"></div><div class="badge"></div><div class="badge"></div><div class="badge"></div><div class="badge"></div>
    </div>
  </div>
</section>

<svg class="footer-wave" viewBox="0 0 1200 40" preserveAspectRatio="none"><path d="M0 40V18C300 -6 900 -6 1200 18V40z" fill="#15263b"/><path d="M0 22C300 0 900 0 1200 22" stroke="#1d86d1" stroke-width="3" fill="none"/></svg>
<footer class="site-footer">
  <div class="wrap footer-cols">
    <div>
      <h5>Quick Links</h5>
      <ul class="links"><li>› Home</li><li>› About Us</li><li>› How it Works</li><li>› Services</li><li>› Training and Transition</li><li>› Contact Us</li></ul>
    </div>
    <div>
      <h5>Contact Details</h5>
      <div class="contact">
        <ul>
          <li><svg width="12" height="16"><path d="M6 1C3 1 1 3 1 6c0 4 5 9 5 9s5-5 5-9c0-3-2-5-5-5z" fill="#1d86d1"/></svg>Brinvale LLC<br>210 Harbor Lane, Suite 4<br>Fairmont, NY 10021</li>
          <li><svg width="14" height="14"><path d="M3 1l3 3-2 2c1 2 2 3 4 4l2-2 3 3-2 2C6 13 1 8 1 3z" fill="#1d86d1"/></svg>1-800-555-0142</li>
          <li><svg width="14" height="14"><path d="M3 1l3 3-2 2c1 2 2 3 4 4l2-2 3 3-2 2C6 13 1 8 1 3z" fill="#1d86d1"/></svg>1-800-555-0143</li>
          <li><svg width="14" height="12"><rect x="1" y="1" width="12" height="10" fill="none" stroke="#1d86d1" stroke-width="1.5"/><path d="M1 1l6 5 6-5" stroke="#1d86d1" stroke-width="1.5" fill="none"/></svg>hello@brinvalecare.example</li>
        </ul>
        <div class="map" role="img" aria-label="Street map showing the office location"></div>
      </div>
    </div>
    <div class="newsletter">
      <h5>Subscribe For Newsletter</h5>
      <p>Stay up to date with our latest news, product updates and agency tips.</p>
      <div class="subscribe"><span>Enter your email</span><b>SUBSCRIBE</b></div>
      <div class="social">Follow Us On: <i></i><i></i><i></i><i></i></div>
    </div>
  </div>
</footer>
<div class="footer-bar">
  <div class="wrap">
    <span>Copyright © 2015 Brinvale LLC. All Rights Reserved.</span>
    <div class="brand"><span class="brand-dot"></span>Brinvale</div>
  </div>
</div>

</body>
</html>
```